Healing stone/crystal Shopify store

Hi - I'm creating a new site to sell healing crystals/stones.Name for the shop is MoonpetalHaven. Site helps people to choose best crystals for them .Shop should have blog aswell.The site should be informative and attractive. Stones we sell Opalite,Green Aventurine,Watermelon Crystal,Rose Quartz Stone,Tiger Eye Stone. Must be Shopify. No content yet, you can fill neccessary fields Lorea Ipsum and if you have some good idea you can put it there
Updates

Designs look the same

Target Market(s)

Woman, English speaking countries.

Industry/Entity Type

Shop

Number of Pages Required

1 page

Colors

Designer to choose colors to be used in the design.

Requirements
Must have
• Blog
Nice to have
• High quality pictures to look site attractive.

```html
<!DOCTYPE html>
<html lang="en">
<head>
<meta charset="utf-8">
<title>Moonpetal Haven – Healing Stones &amp; Crystals</title>
<link href="https://fonts.googleapis.com/css2?family=Oswald:wght@400;500&family=PT+Sans:wght@400;700&display=swap" rel="stylesheet">
<style>
:root{
  --orange:#f7931e;
  --ink:#1c1c1c;
  --text:#444;
  --muted:#777;
  --tile:#eeeeee;
  --line:#dcdcdc;
  --dark:#1e1e1e;
  --footer:#efefef;
  --white:#fff;
}
*{box-sizing:border-box;margin:0;padding:0}
html,body{width:1200px;height:2528px;overflow:hidden}
body{position:relative;background:var(--white);font-family:"PT Sans",Arial,sans-serif;color:var(--text)}
.abs{position:absolute}
.head{font-family:"Oswald","Arial Narrow",sans-serif;color:var(--ink)}
svg{display:block}

/* top bar */
.topbar{left:0;top:0;width:1200px;height:30px;background:var(--orange);color:var(--white);font-size:12px}
.topbar .links{left:199px;top:0;height:30px;display:flex;align-items:center}
.topbar .links span{padding:0 10px;border-left:1px solid rgba(255,255,255,.7);line-height:14px}
.topbar .links span:first-child{border:0;padding-left:0;display:flex;align-items:center;gap:6px}
.topbar .tools{left:960px;top:8px;display:flex;gap:14px}

/* header */
.logo{left:199px;top:44px;font-size:27px;font-weight:500}
.nav{left:540px;top:30px;height:64px;display:flex;align-items:center;font-family:"Oswald",sans-serif;font-size:12px;color:var(--ink)}
.nav a{text-decoration:none;color:inherit;margin-right:30px;letter-spacing:.3px}
.nav .home{position:relative;padding-right:0}
.nav .home::after{content:"";position:absolute;right:-16px;top:-20px;width:2px;height:48px;background:var(--orange)}
.nav .cart{margin-left:4px}

/* hero */
.hero{left:0;top:94px;width:674px;height:449px;background:radial-gradient(circle at 45% 45%,#8a6b62 0,#5a5552 35%,#3d3c3a 100%)}
.hero-title{left:0;top:228px;width:840px;text-align:center;font-size:56px;font-weight:500;color:var(--white)}
.hero-sub{left:0;top:302px;width:840px;text-align:center;font-size:15px;color:var(--white);font-weight:700}
.hero-link{left:377px;top:339px;font-size:13px;color:var(--white);font-weight:700;border-bottom:1px solid var(--white);padding-bottom:3px}
.hero-note{left:200px;top:495px;font-size:14px;color:var(--white);font-weight:700}
.hero-arrows{left:539px;top:487px;display:flex;gap:4px}
.hero-arrows div{width:53px;height:36px;background:var(--white);display:flex;align-items:center;justify-content:center}

.tile{background:var(--tile)}
.tile .ph{position:absolute}
.tile .name{position:absolute;font-family:"Oswald",sans-serif;font-size:13px;color:var(--ink)}
.tile .view{position:absolute;font-size:11px;color:var(--ink);border-bottom:1px solid #999;padding:0 12px 3px}

.divider{left:0;top:588px;width:1200px;height:2px;background:#e4e4e4}

/* promo */
.promo{width:248px;height:300px}
.promo-cap{font-size:13px;color:var(--text)}
.shop-now{left:546px;top:758px;width:105px;height:40px;background:var(--white);font-family:"Oswald",sans-serif;font-size:12px;color:var(--ink);display:flex;align-items:center;justify-content:center}

/* section titles */
.sec-title{left:0;width:1200px;text-align:center;font-size:25px;font-weight:500}
.sec-rule{left:526px;width:148px;height:2px;background:var(--orange)}
.sec-rule::after{content:"";position:absolute;left:68px;top:2px;border:6px solid transparent;border-top-color:var(--orange)}
.sec-sub{left:0;width:1200px;text-align:center;font-size:13px;color:#333}

/* products */
.prod{width:192px;height:236px;background:var(--tile)}
.prod.hover{background:#777}
.prod-name{font-family:"Oswald",sans-serif;font-size:11px;color:var(--ink)}
.prod-price{font-family:"Oswald",sans-serif;font-size:11px;color:var(--ink)}
.prod-icons{left:44px;top:1333px;width:192px;display:flex;justify-content:center;gap:9px}
.prod-icons div{width:30px;height:30px;background:#111;display:flex;align-items:center;justify-content:center}
.slide-btn{top:1235px;width:50px;height:42px;background:#111;display:flex;align-items:center;justify-content:center}

/* blog */
.blog-img{width:257px;height:177px}
.blog-card{width:222px;height:131px;background:var(--white);padding:10px 18px 0}
.blog-meta{display:flex;gap:16px;font-size:10px;color:#555;border-bottom:1px solid var(--line);padding-bottom:6px}
.blog-meta span{display:flex;align-items:center;gap:5px}
.blog-title{margin-top:10px;font-size:13.5px;line-height:17px;font-weight:700;color:var(--ink)}
.blog-text{width:210px;font-size:10.5px;line-height:17px;color:#555}

/* newsletter */
.newsletter{left:0;top:1918px;width:1200px;height:271px;background:linear-gradient(135deg,#2a2a2a 0,#161616 50%,#262626 100%)}
.news-title{left:0;top:1976px;width:1200px;text-align:center;font-size:21px;color:var(--white)}
.news-form{left:369px;top:2035px;width:472px;height:44px;background:var(--white);display:flex;align-items:center}
.news-form .ico{width:68px;height:100%;display:flex;align-items:center;justify-content:center;border-right:1px solid var(--line)}
.news-form .field{flex:1;padding-left:22px;font-size:11px;color:#666;letter-spacing:.3px}
.news-form .go{width:50px;display:flex;justify-content:center}
.social{top:2104px;width:40px;height:40px}

/* footer */
.footer{left:0;top:2189px;width:1200px;height:291px;background:linear-gradient(160deg,#f4f4f4 0,#e8e8e8 50%,#f2f2f2 100%)}
.foot-brand{left:199px;top:2250px;font-size:21px}
.foot-row{left:199px;display:flex;align-items:center;gap:20px;font-size:12px;color:#333;line-height:17px}
.foot-row .dia{width:34px;height:34px;flex:none}
.foot-col h4{font-family:"Oswald",sans-serif;font-weight:400;font-size:14px;color:var(--ink);margin-bottom:20px}
.foot-col li{list-style:none;font-size:12px;color:#333;line-height:24px}
.copy{left:0;top:2480px;width:1200px;height:48px;background:var(--white);border-top:1px solid #cfcfcf;text-align:center;line-height:46px;font-size:12px;color:#333}
</style>
</head>
<body>

<!-- Top bar -->
<div class="abs topbar">
  <div class="abs links">
    <span><svg width="12" height="12" viewBox="0 0 12 12"><circle cx="6" cy="3.5" r="3" fill="#fff"/><path d="M0 12c0-4 3-5.5 6-5.5s6 1.5 6 5.5z" fill="#fff"/></svg>My Account</span>
    <span>Our Location</span><span>Contact Us</span><span>Cart</span>
  </div>
  <div class="abs tools">
    <svg width="14" height="14" viewBox="0 0 24 24"><path d="M12 21s-8-5.3-8-11a4.5 4.5 0 0 1 8-2.8A4.5 4.5 0 0 1 20 10c0 5.7-8 11-8 11z" fill="#fff"/></svg>
    <svg width="14" height="14" viewBox="0 0 24 24"><circle cx="10" cy="10" r="6.5" fill="none" stroke="#fff" stroke-width="2.6"/><path d="M15 15l6 6" stroke="#fff" stroke-width="2.6"/></svg>
  </div>
</div>

<!-- Header -->
<div class="abs head logo">Moonpetal Haven</div>
<nav class="abs nav">
  <svg width="22" height="18" viewBox="0 0 22 18" style="margin-right:10px"><path d="M11 1L1 9h3v8h5v-5h4v5h5V9h3z" fill="#222"/></svg>
  <a class="home" href="#">HOME</a>
  <a href="#" style="margin-left:8px">ABOUT US</a>
  <a href="#">PRODUCT</a>
  <a href="#">BLOG</a>
  <a href="#">CONTACT US</a>
  <svg class="cart" width="18" height="16" viewBox="0 0 24 20" style="margin-left:40px"><path d="M1 2h4l3 11h12l2-8H7" fill="none" stroke="#f7931e" stroke-width="2.4"/><circle cx="9" cy="17" r="1.8" fill="#f7931e"/><circle cx="19" cy="17" r="1.8" fill="#f7931e"/></svg>
</nav>

<!-- Hero -->
<div class="abs hero" role="img" aria-label="Close-up of smooth river pebbles with a red heart-shaped stone"></div>
<div class="abs head hero-title">Moonpetal Haven</div>
<div class="abs hero-sub" style="font-family:'Oswald',sans-serif;font-weight:400">Shop Moonpetal Haven Today</div>
<div class="abs hero-link">View Collection</div>
<div class="abs hero-note">Lorem Ipsum is simply dummy text of the printing..</div>
<div class="abs hero-arrows">
  <div><svg width="18" height="12" viewBox="0 0 18 12"><path d="M17 6H2M6 1L1 6l5 5" fill="none" stroke="#111" stroke-width="2"/></svg></div>
  <div><svg width="18" height="12" viewBox="0 0 18 12"><path d="M1 6h15M12 1l5 5-5 5" fill="none" stroke="#111" stroke-width="2"/></svg></div>
</div>

<div class="abs tile" style="left:698px;top:94px;width:291px;height:213px">
  <div class="ph" role="img" aria-label="Pink carved crystal elephant" style="left:26px;top:18px;width:170px;height:130px;background:radial-gradient(ellipse,#e5a9c4 0,#d690b3 55%,rgba(238,238,238,0) 75%)"></div>
  <div class="name" style="left:171px;top:148px">Green Aventurine</div>
  <div class="view" style="left:161px;top:172px">View Collection</div>
</div>
<div class="abs tile" style="left:698px;top:330px;width:291px;height:213px">
  <div class="ph" role="img" aria-label="Two carved tiger eye elephants" style="left:14px;top:18px;width:210px;height:130px;background:radial-gradient(ellipse,#6b3b1f 0,#4a2a17 50%,rgba(238,238,238,0) 75%)"></div>
  <div class="name" style="left:227px;top:150px">Opalite</div>
  <div class="view" style="left:181px;top:174px">View Collection</div>
</div>
<div class="abs tile" style="left:1011px;top:94px;width:189px;height:449px">
  <div class="ph" role="img" aria-label="Dark blue carved crystal angel" style="left:8px;top:50px;width:150px;height:220px;background:radial-gradient(ellipse,#2d2f63 0,#1f2149 50%,rgba(238,238,238,0) 75%)"></div>
  <div class="name" style="left:51px;top:345px">Tiger Eye Stone</div>
  <div class="view" style="left:45px;top:368px">View Collection</div>
</div>

<div class="abs divider"></div>

<!-- Promo -->
<div class="abs promo" role="img" aria-label="Ring of carved crystal angels in many colours on a dark background" style="left:199px;top:628px;background:radial-gradient(circle,#2a2a2a 0,#2a2a2a 30%,#c9b8c8 55%,#9fb4c8 80%,#6f7b68 100%)"></div>
<div class="abs promo" role="img" aria-label="Polished tiger eye stone on black" style="left:475px;top:628px;background:radial-gradient(ellipse at 50% 35%,#b5843e 0,#6b4420 35%,#0d0d0d 70%)"></div>
<div class="abs shop-now">SHOP NOW</div>
<div class="abs promo" role="img" aria-label="Pile of colourful polished tumbled stones" style="left:752px;top:628px;background:linear-gradient(135deg,#c24b2c 0,#c59a2e 30%,#2f7a4a 55%,#6a8fc0 75%,#3b2a22 100%)"></div>
<div class="abs promo-cap" style="left:199px;top:940px">Sale healing stones and crystal</div>
<div class="abs promo-cap" style="left:475px;top:940px">Sale healing stones and crystal</div>
<div class="abs promo-cap" style="left:752px;top:940px">Sale healing stones and crystal</div>

<!-- Our Product -->
<div class="abs head sec-title" style="top:1025px">OUR PRODUCT</div>
<div class="abs sec-rule" style="top:1066px"></div>
<div class="abs sec-sub" style="top:1085px">Lorem Ipsum is simply dummy text of the printing and typesetting industry.</div>

<div class="abs prod hover" style="left:44px;top:1139px"><div role="img" aria-label="Green carved opalite elephant" style="position:absolute;left:36px;top:50px;width:120px;height:90px;background:radial-gradient(ellipse,#3f6b55 0,#4d6358 55%,rgba(119,119,119,0) 75%)"></div></div>
<div class="abs prod-icons">
  <div><svg width="14" height="14" viewBox="0 0 24 24"><path d="M12 21s-8-5.3-8-11a4.5 4.5 0 0 1 8-2.8A4.5 4.5 0 0 1 20 10c0 5.7-8 11-8 11z" fill="#fff"/></svg></div>
  <div><svg width="14" height="14" viewBox="0 0 24 24"><path d="M3 9V3h6M15 3h6v6M21 15v6h-6M9 21H3v-6" fill="none" stroke="#fff" stroke-width="2.5"/></svg></div>
  <div><svg width="16" height="14" viewBox="0 0 24 20"><path d="M1 2h4l3 11h12l2-8H7" fill="none" stroke="#fff" stroke-width="2.4"/><circle cx="9" cy="17" r="1.8" fill="#fff"/><circle cx="19" cy="17" r="1.8" fill="#fff"/></svg></div>
</div>
<div class="abs prod" style="left:275px;top:1139px"><div role="img" aria-label="Pink carved aventurine elephants" style="position:absolute;left:20px;top:65px;width:155px;height:90px;background:radial-gradient(ellipse,#e2707a 0,#d9848a 50%,rgba(238,238,238,0) 75%)"></div></div>
<div class="abs prod" style="left:504px;top:1139px"><div role="img" aria-label="Carved watermelon crystal angel" style="position:absolute;left:50px;top:30px;width:92px;height:170px;background:radial-gradient(ellipse,#9a6a2c 0,#7a5226 50%,rgba(238,238,238,0) 75%)"></div></div>
<div class="abs prod" style="left:733px;top:1139px"><div role="img" aria-label="Two carved rose quartz elephants" style="position:absolute;left:12px;top:60px;width:170px;height:100px;background:radial-gradient(ellipse,#4a2a17 0,#5b3520 50%,rgba(238,238,238,0) 75%)"></div></div>
<div class="abs prod" style="left:961px;top:1139px"><div role="img" aria-label="Two carved rose quartz elephants" style="position:absolute;left:12px;top:60px;width:170px;height:100px;background:radial-gradient(ellipse,#4a2a17 0,#5b3520 50%,rgba(238,238,238,0) 75%)"></div></div>

<div class="abs slide-btn" style="left:0"><svg width="18" height="12" viewBox="0 0 18 12"><path d="M17 6H2M6 1L1 6l5 5" fill="none" stroke="#fff" stroke-width="2.2"/></svg></div>
<div class="abs slide-btn" style="left:1150px"><svg width="18" height="12" viewBox="0 0 18 12"><path d="M1 6h15M12 1l5 5-5 5" fill="none" stroke="#fff" stroke-width="2.2"/></svg></div>

<div class="abs prod-name" style="left:44px;top:1386px">OPALITE</div><div class="abs prod-price" style="left:204px;top:1386px">$95.00</div>
<div class="abs prod-name" style="left:275px;top:1386px">GREEN AVENTURINE</div><div class="abs prod-price" style="left:434px;top:1386px">$95.00</div>
<div class="abs prod-name" style="left:504px;top:1386px">WATERMELON CRYSTAL</div><div class="abs prod-price" style="left:664px;top:1386px">$95.00</div>
<div class="abs prod-name" style="left:733px;top:1386px">ROSE QUARTZ STONE</div><div class="abs prod-price" style="left:893px;top:1386px">$95.00</div>
<div class="abs prod-name" style="left:961px;top:1386px">ROSE QUARTZ STONE</div><div class="abs prod-price" style="left:1122px;top:1386px">$95.00</div>

<!-- Blog -->
<div class="abs head sec-title" style="top:1468px">BLOG POST</div>
<div class="abs sec-rule" style="top:1509px"></div>
<div class="abs sec-sub" style="top:1528px">Lorem Ipsum is simply dummy text of the printing and typesetting industry.</div>

<div class="abs blog-img" role="img" aria-label="Colourful polished gemstones close-up" style="left:200px;top:1592px;background:linear-gradient(120deg,#d23a6a 0,#2bb3b0 35%,#c2272d 70%,#6b1e1e 100%)"></div>
<div class="abs blog-img" role="img" aria-label="Ring of carved crystal angels" style="left:472px;top:1592px;background:linear-gradient(120deg,#8a6038 0,#d8d4d6 35%,#a9c0de 70%,#6e8a74 100%)"></div>
<div class="abs blog-img" role="img" aria-label="Assorted tumbled crystals on black" style="left:743px;top:1592px;background:linear-gradient(120deg,#101010 0,#b23a2a 35%,#c79a3a 55%,#3a7ab0 75%,#101010 100%)"></div>

<div class="abs blog-card" style="left:200px;top:1714px"></div>
<div class="abs blog-card" style="left:472px;top:1714px"></div>
<div class="abs blog-card" style="left:743px;top:1714px"></div>

<div class="abs" style="left:216px;top:1724px;width:205px">
  <div class="blog-meta"><span><svg width="11" height="11" viewBox="0 0 12 12"><rect x="1" y="2" width="10" height="9" fill="none" stroke="#666"/><path d="M1 5h10" stroke="#666"/></svg>2018-03-02</span><span><svg width="12" height="11" viewBox="0 0 12 11"><path d="M1 1h10v7H5l-3 2V8H1z" fill="none" stroke="#666"/></svg>2 Comments</span></div>
  <div class="blog-title">Lorem Ipsum is simply dummy text of the text..</div>
  <p class="blog-text" style="margin-top:12px">Lorem Ipsum is simply dummy text ofthe printing and typesettinindustr Loremlp-sum text indusry......</p>
</div>
<div class="abs" style="left:488px;top:1724px;width:205px">
  <div class="blog-meta"><span><svg width="11" height="11" viewBox="0 0 12 12"><rect x="1" y="2" width="10" height="9" fill="none" stroke="#666"/><path d="M1 5h10" stroke="#666"/></svg>2018-03-02</span><span><svg width="12" height="11" viewBox="0 0 12 11"><path d="M1 1h10v7H5l-3 2V8H1z" fill="none" stroke="#666"/></svg>2 Comments</span></div>
  <div class="blog-title">Lorem Ipsum is simply dummy text of the text..</div>
  <p class="blog-text" style="margin-top:12px">Lorem Ipsum is simply dummy text ofthe printing and typesettinindustr Loremlp-sum text indusry......</p>
</div>
<div class="abs" style="left:759px;top:1724px;width:205px">
  <div class="blog-meta"><span><svg width="11" height="11" viewBox="0 0 12 12"><rect x="1" y="2" width="10" height="9" fill="none" stroke="#666"/><path d="M1 5h10" stroke="#666"/></svg>2018-03-02</span><span><svg width="12" height="11" viewBox="0 0 12 11"><path d="M1 1h10v7H5l-3 2V8H1z" fill="none" stroke="#666"/></svg>2 Comments</span></div>
  <div class="blog-title">Lorem Ipsum is simply dummy text of the text..</div>
  <p class="blog-text" style="margin-top:12px">Lorem Ipsum is simply dummy text ofthe printing and typesettinindustr Loremlp-sum text indusry......</p>
</div>

<!-- Newsletter -->
<div class="abs newsletter"></div>
<div class="abs head news-title">SUBSCRIBE NEWSLETTER</div>
<div class="abs news-form">
  <div class="ico"><svg width="20" height="14" viewBox="0 0 20 14"><rect x="1" y="1" width="18" height="12" fill="none" stroke="#f7931e" stroke-width="1.6"/><path d="M1 1l9 7 9-7" fill="none" stroke="#f7931e" stroke-width="1.6"/></svg></div>
  <div class="field">ENTER YOUR E-MAIL ADDRESS</div>
  <div class="go"><svg width="16" height="12" viewBox="0 0 18 12"><path d="M1 6h15M12 1l5 5-5 5" fill="none" stroke="#111" stroke-width="2.2"/></svg></div>
</div>
<svg class="abs social" style="left:519px" viewBox="0 0 40 40"><rect x="8" y="8" width="24" height="24" transform="rotate(45 20 20)" fill="none" stroke="#999"/><circle cx="20" cy="20" r="3" fill="#f7931e"/></svg>
<svg class="abs social" style="left:585px" viewBox="0 0 40 40"><rect x="8" y="8" width="24" height="24" transform="rotate(45 20 20)" fill="none" stroke="#999"/><circle cx="20" cy="20" r="3" fill="#f7931e"/></svg>
<svg class="abs social" style="left:649px" viewBox="0 0 40 40"><rect x="8" y="8" width="24" height="24" transform="rotate(45 20 20)" fill="none" stroke="#999"/><circle cx="20" cy="20" r="3" fill="#f7931e"/></svg>

<!-- Footer -->
<div class="abs footer"></div>
<div class="abs head foot-brand">Moonpetal Haven</div>
<div class="abs foot-row" style="top:2299px">
  <svg class="dia" viewBox="0 0 34 34"><rect x="7" y="7" width="20" height="20" transform="rotate(45 17 17)" fill="none" stroke="#888"/><path d="M13 12l3 0 1 3-2 1c1 2 2 3 4 4l1-2 3 1 0 3c-6 0-10-4-10-10z" fill="#f7931e"/></svg>
  <span>+1234566789</span>
</div>
<div class="abs foot-row" style="top:2349px">
  <svg class="dia" viewBox="0 0 34 34"><rect x="7" y="7" width="20" height="20" transform="rotate(45 17 17)" fill="none" stroke="#888"/><path d="M17 24s-5-5-5-9a5 5 0 0 1 10 0c0 4-5 9-5 9z" fill="#f7931e"/><circle cx="17" cy="15" r="1.8" fill="#fff"/></svg>
  <span>Lorem Ipsum is simply dummy text of<br>the printing and text..</span>
</div>
<div class="abs foot-row" style="top:2410px">
  <svg class="dia" viewBox="0 0 34 34"><rect x="7" y="7" width="20" height="20" transform="rotate(45 17 17)" fill="none" stroke="#888"/><rect x="11" y="13" width="12" height="8" fill="none" stroke="#f7931e" stroke-width="1.5"/><path d="M11 13l6 5 6-5" fill="none" stroke="#f7931e" stroke-width="1.5"/></svg>
  <span>info@moonpetalhaven.com</span>
</div>

<div class="abs foot-col" style="left:504px;top:2255px"><h4>Quick Links</h4><ul><li>Home</li><li>About Us</li><li>Product</li><li>Blog</li><li>Contact Us</li></ul></div>
<div class="abs foot-col" style="left:610px;top:2255px"><h4>My Account</h4><ul><li>Sign In</li><li>View Cart</li><li>My Wishlist</li><li>Shipping &amp; Returns</li><li>Help</li></ul></div>
<div class="abs foot-col" style="left:758px;top:2255px"><h4>Customer Care</h4><ul><li>Returns</li><li>FAQ's</li><li>Care &amp; Warranty</li><li>Contact Us</li></ul></div>
<div class="abs foot-col" style="left:888px;top:2255px"><h4>&nbsp;</h4><ul><li>Privacy Policy</li><li>Terms and Condition</li></ul></div>

<div class="abs copy">© Copyright 2018 MoonpetalHaven. All Rights Reserved.</div>

</body>
</html>
```